Need a book cover design for a Vellora Book on Herbal Remedies

I need a book cover for my new ebook, here are the details:
Title: Meadow Tonics
Sub-Heading: Old Garden Wisdom Notes
Finding the Quiet Strength of the Wild for Daily Balance and Calm
Author: Mara Delacroix

```html
<!DOCTYPE html>
<html lang="en">
<head>
<meta charset="utf-8">
<title>Meadow Tonics – Mara Delacroix</title>
<link rel="stylesheet" href="https://fonts.googleapis.com/css2?family=Bebas+Neue&family=Montserrat:wght@400;600&family=Varela+Round&display=swap">
<style>
  :root {
    --backdrop: #d4d4d4;
    --plum: #5f124b;
    --ink: #000000;
    --sun: #fcd800;
    --paper: #ffffff;
    --cobalt: #315fac;
    --sub-text: #e3d9e0;
  }
  html, body {
    margin: 0;
    padding: 0;
    width: 1200px;
    height: 1200px;
    overflow: hidden;
    background: var(--backdrop);
  }
  .cover {
    position: absolute;
    left: 230px;
    top: 44px;
    width: 740px;
    height: 1112px;
    background: var(--ink);
  }
  .subtitle-panel {
    position: absolute;
    left: 0;
    top: 0;
    width: 270px;
    height: 346px;
    background: var(--plum);
  }
  .subtitle {
    position: absolute;
    right: 14px;
    top: 114px;
    margin: 0;
    text-align: right;
    font-family: "Varela Round", "Montserrat", sans-serif;
    font-size: 24px;
    line-height: 31px;
    color: var(--sub-text);
    font-weight: 400;
  }
  .subtitle strong {
    font-family: "Montserrat", sans-serif;
    font-weight: 600;
    letter-spacing: 0.2px;
  }
  .photo-apothecary {
    position: absolute;
    left: 270px;
    top: 0;
    width: 470px;
    height: 346px;
    background:
      radial-gradient(ellipse at 30% 65%, rgba(214,168,72,0.85), transparent 40%),
      radial-gradient(ellipse at 75% 60%, rgba(196,200,96,0.8), transparent 38%),
      radial-gradient(ellipse at 52% 62%, rgba(150,70,100,0.7), transparent 30%),
      radial-gradient(ellipse at 20% 10%, rgba(150,160,140,0.9), transparent 40%),
      linear-gradient(180deg, #5a4a3a 0%, #6f7a4a 45%, #8a7b5e 80%, #6b5a48 100%);
  }
  .title-band {
    position: absolute;
    left: 0;
    top: 346px;
    width: 740px;
    height: 528px;
  }
  .title-band text {
    font-family: "Bebas Neue", "Oswald", sans-serif;
  }
  .photo-meadow {
    position: absolute;
    left: 0;
    top: 874px;
    width: 370px;
    height: 238px;
    background:
      radial-gradient(ellipse at 75% 20%, rgba(230,225,190,0.8), transparent 45%),
      radial-gradient(ellipse at 40% 45%, rgba(190,160,150,0.5), transparent 35%),
      linear-gradient(180deg, #8c9a6a 0%, #6f8a4c 50%, #52733a 100%);
  }
  .author-panel {
    position: absolute;
    left: 370px;
    top: 874px;
    width: 370px;
    height: 238px;
    background: var(--cobalt);
    display: flex;
    align-items: center;
    justify-content: center;
  }
  .author {
    margin: 0;
    font-family: "Montserrat", sans-serif;
    font-weight: 600;
    font-size: 52px;
    line-height: 54px;
    color: var(--paper);
    text-align: left;
    letter-spacing: 1px;
  }
</style>
</head>
<body>
  <main class="cover">
    <section class="subtitle-panel">
      <p class="subtitle"><strong>Old Garden<br>Wisdom Notes</strong><br>Finding the<br>Quiet Strength<br>of the Wild for<br>Daily Balance<br>and Calm</p>
    </section>
    <div class="photo-apothecary" role="img" aria-label="Glass jars with cork stoppers filled with dried herbs and flowers on a rustic wooden table"></div>

    <svg class="title-band" viewBox="0 0 740 528" xmlns="http://www.w3.org/2000/svg" aria-label="Meadow Tonics">
      <rect width="740" height="528" fill="var(--ink)"/>
      <text x="42" y="308" font-size="300" fill="var(--sun)" textLength="656" lengthAdjust="spacingAndGlyphs">MEADOW</text>
      <text x="42" y="522" font-size="282" fill="var(--paper)" textLength="656" lengthAdjust="spacingAndGlyphs">TONICS</text>
    </svg>

    <div class="photo-meadow" role="img" aria-label="Flowering mint and herb plants in a sunlit garden"></div>
    <section class="author-panel">
      <p class="author">MARA<br>DELACROIX</p>
    </section>
  </main>
</body>
</html>
```